IT Company based on Biology Business Needs a Business Card Design

We need a business card design for a new company called 'Lumen CELL'. We develop the machine learning solutions especially focused on deep learning algorithms for biology industry. Our initial product is a vision detection on biological images to help doctors diagnose the symptoms. We would like to see designs that use the color green.

Industry/Entity Type

Business

```html
<!DOCTYPE html>
<html lang="en">
<head>
<meta charset="utf-8">
<title>Lumen CELL — Business Card</title>
<link href="https://fonts.googleapis.com/css2?family=Lato:wght@400;700&display=swap" rel="stylesheet">
<style>
  :root {
    --leaf: #7bc142;
    --forest: #0b8a3e;
    --paper: #ffffff;
    --paper-shade: #eef0ee;
    --backdrop: #e9e6e1;
  }
  * { margin: 0; padding: 0; box-sizing: border-box; }
  html, body { width: 1200px; height: 900px; overflow: hidden; }
  body {
    background: var(--backdrop);
    font-family: "Lato", sans-serif;
    position: relative;
  }
  .card {
    position: absolute;
    top: 300px;
    width: 520px;
    height: 300px;
    box-shadow: 0 6px 18px rgba(0,0,0,0.18);
    overflow: hidden;
  }
  .card-front { left: 50px; background: var(--leaf); }
  .card-back { left: 630px; background: linear-gradient(180deg, var(--paper-shade), var(--paper) 40%); }

  .brand {
    display: flex;
    align-items: center;
    gap: 14px;
    position: absolute;
    font-weight: 700;
    letter-spacing: 0.5px;
  }
  .card-front .brand {
    left: 50%; top: 50%;
    transform: translate(-50%, -50%);
    color: var(--paper);
    font-size: 56px;
  }
  .card-front .brand-dot { width: 30px; height: 30px; border-radius: 50%; background: var(--paper); }
  .card-back .brand {
    left: 50%; top: 70px;
    transform: translate(-50%, -50%);
    color: var(--leaf);
    font-size: 40px;
  }
  .card-back .brand-dot { width: 22px; height: 22px; border-radius: 50%; background: var(--forest); }

  .contact-band {
    position: absolute;
    left: 0; right: 0; bottom: 0;
    height: 152px;
    background: var(--leaf);
    border-top: 6px solid var(--forest);
    box-shadow: 0 -6px 0 var(--paper), 0 -12px 0 var(--leaf);
    display: flex;
    color: var(--paper);
    padding: 16px 24px 0;
  }
  .person {
    flex: 1;
    text-align: center;
    padding-top: 8px;
  }
  .person-name { font-size: 22px; font-weight: 700; }
  .person-role { font-size: 14px; margin-top: 2px; }
  .person-address { font-size: 15px; margin-top: 12px; line-height: 1.35; }
  .contact-list {
    list-style: none;
    width: 200px;
    font-size: 14px;
    padding-top: 6px;
  }
  .contact-list li { display: flex; align-items: center; gap: 8px; margin-bottom: 6px; }
  .contact-icon { width: 16px; height: 16px; flex: none; }
</style>
</head>
<body>
  <section class="card card-front" aria-label="Business card front">
    <div class="brand"><span class="brand-dot"></span><span class="brand-name">Lumen CELL</span></div>
  </section>

  <section class="card card-back" aria-label="Business card back">
    <div class="brand"><span class="brand-dot"></span><span class="brand-name">Lumen CELL</span></div>
    <div class="contact-band">
      <div class="person">
        <p class="person-name">Mara Holt</p>
        <p class="person-role">Managing Director</p>
        <p class="person-address">88 Harbor Lane, Newport<br>Region, 40211</p>
      </div>
      <ul class="contact-list">
        <li>
          <svg class="contact-icon" viewBox="0 0 16 16"><rect width="16" height="16" rx="2" fill="#fff"/><path d="M4 5c0 4 3 7 7 7l1-2-2-1-1 1c-1-.5-2-1.5-2.5-2.5l1-1-1-2z" fill="#7bc142"/></svg>
          555-014-2880
        </li>
        <li>
          <svg class="contact-icon" viewBox="0 0 16 16"><rect width="16" height="16" rx="2" fill="#fff"/><rect x="4" y="6" width="8" height="6" fill="#7bc142"/><rect x="5.5" y="3.5" width="5" height="3" fill="none" stroke="#7bc142"/></svg>
          555-014-2881
        </li>
        <li>
          <svg class="contact-icon" viewBox="0 0 16 16"><rect width="16" height="16" rx="2" fill="#fff"/><rect x="3.5" y="5" width="9" height="6" fill="none" stroke="#7bc142"/><path d="M3.5 5l4.5 3.5L12.5 5" fill="none" stroke="#7bc142"/></svg>
          hello@lumencell.bio
        </li>
        <li>
          <svg class="contact-icon" viewBox="0 0 16 16"><rect width="16" height="16" rx="2" fill="#fff"/><path d="M6 10l4-4M5 8.5l-1 1a1.8 1.8 0 002.5 2.5l1-1M11 7.5l1-1A1.8 1.8 0 009.5 4l-1 1" fill="none" stroke="#7bc142" stroke-width="1.3"/></svg>
          www.lumencell.bio
        </li>
      </ul>
    </div>
  </section>
</body>
</html>
```